◆遺体の目的/概要
電子書籍(novrel)の表紙のデザインをお願いします。

◆画像のサイズ
表紙ファイルの理想的な寸法は2,560✕1,600ピクセルです。
注:画像の寸法は1,000✕625ピクセル以上であることが必要です。
画像の最大の寸法は10,000✕10,000ピクセルです。

◆タイトル
外国人と一緒に働くすべての人へ
「ソラーレ・ポルト・メトリクス」
Solare Porto Metrics
少子高齢化の社会を生き残る強い会社を作る方法

◆著者
外国人ブリッジコーディネーター
橋本 健吾

◆本の内容
少子高齢化が進む社会にあって、
外国人労働者の必要性や、彼らが働きやす職場環境作りの必要性
どんなコミュニケーションが必要かという事を解説した本です。
※本文を参考資料として添付します。

◆デザイン要望
会社や企業向けなので、プロフェッショナルなイメージ
グローバルなイメージ(目を引く外国人の写真など)
でよろしくお願い致します。

※次点、次々点の方への参加報酬も設定いたします。

※その他、必要な情報がありましたらお問い合せください。

本文の内容に該当する登場人物のイメージを用いている点や
「強い会社を作る」という主なテーマが強調されていいる点など、
ぱっと見て分かりやすいものを選ばせていただきました。

ほんとにどれもセンスを感じられるものだったので、
選定するのに、とても時間がかかりました。
同じテーマで、こんなにも色々なアイデアがあること
その多様性に感動しました。
皆さんが時間をかけて、考えてくださったことに感謝致します。
今後も出版を考えていますので、また依頼の際は多くの方の提案をよろしくお願い致します!

```html
<!DOCTYPE html>
<html lang="ja">
<head>
<meta charset="utf-8">
<title>ソラーレ・ポルト・メトリクス</title>
<link rel="stylesheet" href="https://fonts.googleapis.com/css2?family=Noto+Sans+JP:wght@900&family=Noto+Serif+JP:wght@500;700;900&family=Cormorant+Garamond:wght@500&display=swap">
<style>
  :root {
    --navy: #0d1f45;
    --navy-soft: #1e3364;
    --paper: #ffffff;
    --mist: #e9eef6;
    --sky-1: #9fb4d4;
    --sky-2: #dfe8f4;
    --faint: rgba(30, 51, 100, 0.07);
  }
  * { margin: 0; padding: 0; box-sizing: border-box; }
  html, body { width: 749px; height: 1200px; overflow: hidden; background: var(--paper); }
  .cover {
    position: relative;
    width: 749px;
    height: 1200px;
    overflow: hidden;
    background: linear-gradient(180deg, var(--paper) 0%, var(--mist) 100%);
    color: var(--navy);
  }
  .cover-photo {
    position: absolute;
    left: 0; top: 0;
    width: 749px; height: 480px;
    background:
      linear-gradient(180deg, rgba(255,255,255,0) 55%, rgba(255,255,255,0.95) 100%),
      linear-gradient(120deg, var(--sky-1) 0%, var(--sky-2) 45%, #b9c8de 70%, #8fa6c8 100%);
  }
  .world-backdrop {
    position: absolute;
    left: 0; top: 480px;
    width: 749px; height: 720px;
    background: radial-gradient(ellipse at 50% 55%, rgba(200,212,230,0.35) 0%, rgba(255,255,255,0) 70%);
  }
  .deco-word {
    position: absolute;
    font-family: "Cormorant Garamond", serif;
    font-weight: 500;
    color: var(--faint);
    white-space: nowrap;
    line-height: 1;
  }
  .deco-word--right {
    font-size: 92px;
    right: -6px; top: 250px;
    writing-mode: vertical-rl;
  }
  .deco-word--left {
    font-size: 70px;
    left: 10px; top: 520px;
    transform: rotate(-70deg);
    transform-origin: left top;
  }
  .tagline {
    position: absolute;
    top: 370px; left: 0; width: 749px;
    text-align: center;
    font-family: "Noto Serif JP", serif;
    font-weight: 700;
    font-size: 33px;
    line-height: 1.38;
    letter-spacing: 0.06em;
    color: var(--navy);
    text-shadow: 0 0 8px #fff, 0 0 14px #fff;
  }
  .title {
    position: absolute;
    top: 515px; left: 0; width: 749px;
    text-align: center;
    font-family: "Noto Sans JP", sans-serif;
    font-weight: 900;
    font-size: 62px;
    line-height: 1.22;
    letter-spacing: 0.01em;
    color: var(--navy);
  }
  .title-en {
    position: absolute;
    top: 708px; left: 190px;
    width: 370px; height: 118px;
  }
  .title-en svg { position: absolute; inset: 0; }
  .title-en p {
    position: relative;
    text-align: center;
    font-family: "Cormorant Garamond", serif;
    font-weight: 500;
    font-size: 42px;
    line-height: 1.2;
    padding-top: 8px;
    color: var(--navy-soft);
  }
  .subtitle {
    position: absolute;
    top: 852px; left: 0; width: 749px;
    text-align: center;
    font-family: "Noto Serif JP", serif;
    font-weight: 900;
    font-size: 44px;
    line-height: 1.35;
    color: var(--navy);
  }
  .author {
    position: absolute;
    top: 1042px; left: 0; width: 749px;
    text-align: center;
    font-family: "Noto Serif JP", serif;
    color: var(--navy);
  }
  .author-role { font-size: 17px; font-weight: 500; letter-spacing: 0.02em; }
  .author-name { font-size: 40px; font-weight: 700; letter-spacing: 0.08em; margin-top: 6px; padding-left: 80px; }
</style>
</head>
<body>
<div class="cover">
  <div class="cover-photo" role="img" aria-label="国際色豊かなビジネスパーソンのグループ写真"></div>
  <div class="world-backdrop" role="img" aria-label="淡い世界地図の背景"></div>
  <div class="deco-word deco-word--right">Metrics</div>
  <div class="deco-word deco-word--left">Solare Porto</div>

  <p class="tagline">外国人と一緒に<br>働くすべての人へ</p>

  <h1 class="title">ソラーレ・ポルト・<br>メトリクス</h1>

  <div class="title-en">
    <svg width="370" height="118" viewBox="0 0 370 118" aria-hidden="true">
      <path d="M16 3 H3 V115 H16" fill="none" stroke="#1e3364" stroke-width="2.5"/>
      <path d="M354 3 H367 V115 H354" fill="none" stroke="#1e3364" stroke-width="2.5"/>
    </svg>
    <p>Solare Porto<br>Metrics</p>
  </div>

  <p class="subtitle">少子高齢化の社会を生き残る<br>強い会社を作る方法</p>

  <div class="author">
    <p class="author-role">外国人ブリッジコーディネーター</p>
    <p class="author-name">橋本 健吾</p>
  </div>
</div>
</body>
</html>
```